Business card design needed for a security services business.

We provide a wide range of security services from guard personnel to electronic systems.

Industry/Entity Type

Security Industry

Contact Information for Business Card

Brent Holloway, Owner Office: 780.555.0148; Cell: 780.555.0193 Email: brent@korvanshieldgroup.example; Address 20417 163 St Edmonton, AB T5X 2K8

Colors
0054AA
0677BA
7BADD7
CADEEF
E8F1F8

Requirements
Nice to have
• On the back of the card I would like to possible list the services I provide: Guards Mobiles Live Video Surveillance Access Intrusion

```html
<!DOCTYPE html>
<html lang="en">
<head>
<meta charset="utf-8">
<title>Korvan Shield Group – Business Card</title>
<link href="https://fonts.googleapis.com/css2?family=Barlow:wght@400;500;600;700&display=swap" rel="stylesheet">
<style>
  :root {
    --backdrop: #d0d0d0;
    --card: #222222;
    --card-pattern-light: #3a3a3a;
    --card-pattern-dark: #1b1b1b;
    --brand-blue: #0677ba;
    --text-light: #ffffff;
    --service-muted: #9a9a9a;
    --service-bright: #d6d6d6;
  }
  * { margin: 0; padding: 0; box-sizing: border-box; }
  html, body {
    width: 1200px;
    height: 1000px;
    overflow: hidden;
    background: var(--backdrop);
    font-family: "Barlow", Arial, sans-serif;
  }
  .card {
    position: absolute;
    left: 293px;
    width: 614px;
    height: 353px;
    border-radius: 30px;
    background: var(--card);
    overflow: hidden;
    color: var(--text-light);
  }
  .card--front { top: 92px; }
  .card--back { top: 539px; }

  .brand-pattern {
    position: absolute;
    inset: 0;
    background: linear-gradient(135deg, var(--card-pattern-dark) 0%, var(--card-pattern-light) 55%, var(--card-pattern-dark) 100%);
  }
  .services {
    position: absolute;
    top: 50px;
    left: 0;
    width: 100%;
    text-align: center;
    font-weight: 700;
    font-size: 20px;
    line-height: 25px;
    color: var(--service-bright);
  }
  .services .muted { color: var(--service-muted); }

  .brand-name {
    position: absolute;
    font-weight: 700;
    color: var(--text-light);
    text-align: center;
    letter-spacing: 0.5px;
    line-height: 1.05;
  }
  .card--front .brand-name {
    left: 366px;
    top: 238px;
    width: 144px;
    font-size: 18px;
  }
  .card--back .brand-name {
    right: 42px;
    top: 34px;
    width: 140px;
    font-size: 17px;
  }

  .person {
    position: absolute;
    left: 52px;
    top: 102px;
  }
  .person__name {
    font-size: 23px;
    font-weight: 700;
    color: var(--brand-blue);
    line-height: 26px;
  }
  .person__role {
    font-size: 22px;
    font-weight: 400;
    line-height: 24px;
  }
  .person__rule {
    width: 66px;
    height: 3px;
    background: var(--brand-blue);
    margin-top: 6px;
  }
  .address, .contact {
    position: absolute;
    left: 52px;
    font-size: 17px;
    line-height: 22px;
  }
  .address { top: 188px; }
  .contact { top: 253px; }
  .contact .label { color: var(--brand-blue); font-weight: 700; }
  .website {
    position: absolute;
    right: 43px;
    top: 295px;
    font-size: 17px;
  }
  .website strong { font-weight: 700; }
</style>
</head>
<body>
  <section class="card card--front">
    <div class="brand-pattern" role="img" aria-label="Faint repeated brand name pattern across the card"></div>
    <p class="services">
      <span class="muted">Card Acess</span> Systems | Mobile Patrols<br>
      <span class="muted">Security Guards</span> | Video Surveillance Systems
    </p>
    <p class="brand-name">KORVAN SHIELD<br>GROUP</p>
  </section>

  <section class="card card--back">
    <p class="brand-name">KORVAN SHIELD<br>GROUP</p>
    <div class="person">
      <p class="person__name">Brent Holloway</p>
      <p class="person__role">Owner</p>
      <div class="person__rule"></div>
    </div>
    <p class="address">20417 163 St Edmonton,<br>&nbsp;AB T5X 2K8</p>
    <p class="contact">
      <span class="label">Office:</span> 780.555.0148<br>
      <span class="label">Cell:</span> 780.555.0193<br>
      brent@korvanshieldgroup.example
    </p>
    <p class="website"><strong>korvanshieldgroup</strong>.example</p>
  </section>
</body>
</html>
```